Design a visually appealing layout for our company mission and values. I want to create a visually appealing 1 page flyer that presents our company mission and values to clients as well as to our internal team/staff. We will utilize the 1 page flyer in internal and external presentations about our company. We will also use the flyer in sales proposals/marketing packages.

Target Market(s)

Internal team members as well as external prospective clients, existing clients & referral partners

Industry/Entity Type

Financial Service

Colors

Designer to choose colors to be used in the design.

Requirements
Must have
• Should reflect our company brand so I have included our Pantone panel, fonts etc. I have provided our company logo as well which should be part of the branded document
Nice to have
• I would like the presentation to be useable in different formats and to different audiences so something that is more graphic/visual heavy - otherwise it's a lot of words that people don't read.
• Would like to be able to easily include in our corporate template powerpoint presentation.

```html
<!DOCTYPE html>
<html lang="en">
<head>
<meta charset="utf-8">
<title>Summit Pension Partners – Mission &amp; Values</title>
<link rel="stylesheet" href="https://fonts.googleapis.com/css2?family=Lato:wght@400;700;900&display=swap">
<style>
  :root {
    --stage: #d9dbe0;
    --paper: #ffffff;
    --body-bg: #dde6ef;
    --ink: #333a40;
    --ink-soft: #4a5158;
    --brand-blue: #1f6fb3;
    --brand-blue-dark: #1a5f9e;
    --brand-green: #8cc152;
    --teamwork: #5a9a2e;
    --empower: #8cc152;
    --knowledge: #0d3c6e;
    --proactivity: #1f6fb3;
    --dedication: #1e9ad6;
    --security: #a84e14;
    --transparency: #e8961e;
    --ring: #a3acb5;
    --divider: #e3e8ee;
  }
  * { box-sizing: border-box; margin: 0; padding: 0; }
  html, body { width: 1200px; height: 1200px; overflow: hidden; }
  body { background: var(--stage); font-family: "Lato", sans-serif; color: var(--ink); position: relative; }

  .flyer {
    position: absolute; left: 160px; top: 30px;
    width: 910px; height: 1180px;
    transform: scale(0.966); transform-origin: top left;
    background: var(--body-bg);
    box-shadow: 0 10px 30px rgba(0,0,0,.25);
    overflow: hidden;
  }

  /* Header */
  .header { position: absolute; left: 0; top: 0; width: 910px; height: 172px; background: var(--paper); box-shadow: 0 3px 6px rgba(0,0,0,.08); }
  .brand { position: absolute; left: 35px; top: 36px; display: flex; align-items: center; gap: 16px; }
  .brand-square { width: 72px; height: 72px; background: var(--brand-blue); }
  .brand-name { font-size: 24px; font-weight: 400; line-height: 29px; color: var(--ink); letter-spacing: 1px; text-transform: uppercase; }
  .tagline { position: absolute; left: 35px; top: 129px; font-size: 14px; letter-spacing: 3px; color: var(--ink-soft); }
  .title-banner {
    position: absolute; left: 427px; top: 38px; width: 483px; height: 75px;
    background: linear-gradient(90deg, var(--brand-blue) 0%, #2a86b0 45%, var(--brand-green) 100%);
    color: #fff; font-weight: 700; font-size: 44px; line-height: 75px; padding-left: 35px; letter-spacing: .5px;
  }

  /* Labels in boxes */
  .box-heading {
    position: absolute; background: #fff; border: 2px solid #4a5158; border-radius: 3px;
    color: var(--brand-blue); font-weight: 700; text-align: center; letter-spacing: .5px;
  }
  .we-value { left: 332px; top: 212px; width: 237px; height: 48px; font-size: 32px; line-height: 44px; }
  .our-mission { left: 341px; top: 894px; width: 237px; height: 49px; font-size: 32px; line-height: 45px; }

  .wheel { position: absolute; left: 0; top: 0; width: 910px; height: 1180px; }
  .band-label { font-family: "Lato", sans-serif; font-weight: 700; font-size: 19px; fill: #fff; letter-spacing: 1px; }
  .band-label.small { font-size: 17px; }

  .value-copy { position: absolute; font-size: 10.5px; line-height: 12.6px; text-align: center; color: var(--ink); }
  .copy-knowledge    { left: 227px; top: 474px; width: 150px; }
  .copy-proactivity  { left: 380px; top: 396px; width: 150px; }
  .copy-dedication   { left: 537px; top: 457px; width: 150px; }
  .copy-security     { left: 642px; top: 600px; width: 132px; }
  .copy-transparency { left: 644px; top: 722px; width: 122px; }
  .copy-teamwork     { left: 144px; top: 718px; width: 122px; }
  .copy-empowerment  { left: 136px; top: 590px; width: 132px; }

  .mission-art {
    position: absolute; left: 400px; top: 769px; width: 117px; height: 115px; border-radius: 8px;
    background: linear-gradient(160deg, #c9dbe8 0%, #b5d1cf 100%);
  }
  .mission-text { position: absolute; left: 205px; top: 956px; width: 510px; text-align: center; font-size: 15px; line-height: 21px; letter-spacing: .5px; text-transform: uppercase; color: var(--ink-soft); }
  .mission-text strong { color: var(--brand-blue); font-weight: 700; }

  /* Footer */
  .footer { position: absolute; left: 0; top: 1085px; width: 910px; height: 95px; background: linear-gradient(180deg, var(--brand-blue-dark), #2a7fc0); }
  .web-bar { position: absolute; left: 230px; top: 1060px; width: 442px; height: 48px; background: var(--brand-green); color: #fff; font-weight: 700; font-size: 26px; line-height: 48px; text-align: center; }
  .social { position: absolute; top: 1062px; width: 46px; height: 46px; border-radius: 50%; background: #fff; border: 3px solid var(--brand-blue); }
  .social.one { left: 698px; } .social.two { left: 752px; } .social.three { left: 806px; }
  .contact { position: absolute; top: 1128px; left: 35px; display: flex; align-items: center; gap: 14px; color: #fff; font-size: 18px; }
  .contact-item { display: flex; align-items: center; gap: 10px; margin-right: 8px; }
  .contact-icon { width: 26px; height: 26px; }
</style>
</head>
<body>
<div class="flyer">

  <header class="header">
    <div class="brand">
      <div class="brand-square"></div>
      <div class="brand-name">Summit<br>Pension<br>Partners</div>
    </div>
    <div class="tagline">BE THE LEADER. PLAN FOR THE FUTURE.</div>
    <div class="title-banner">MISSION &amp; VALUES</div>
  </header>

  <div class="box-heading we-value">WE VALUE:</div>

  <svg class="wheel" viewBox="0 0 910 1180" xmlns="http://www.w3.org/2000/svg">
    <defs>
      <filter id="soft-shadow" x="-10%" y="-10%" width="120%" height="120%">
        <feDropShadow dx="0" dy="4" stdDeviation="8" flood-color="#000" flood-opacity=".15"/>
      </filter>
      <path id="label-arc" d="M163.2 893.8 A352 352 0 1 1 746.8 893.8"/>
      <path id="label-arc-outer" d="M150.8 902.2 A367 367 0 1 1 759.2 902.2"/>
      <path id="label-arc-inner" d="M170.7 888.8 A343 343 0 1 1 739.3 888.8"/>
    </defs>

    <!-- white shell -->
    <path d="M455 697 L112.6 927.9 A413 413 0 1 1 797.4 927.9 Z" fill="#fff" filter="url(#soft-shadow)"/>

    <!-- segment dividers -->
    <g stroke="var(--divider)" stroke-width="2">
      <line x1="272" y1="697" x2="42" y2="697"/>
      <line x1="307" y1="589.4" x2="121" y2="454"/>
      <line x1="398.5" y1="522.9" x2="327.4" y2="304.2"/>
      <line x1="511.5" y1="522.9" x2="582.6" y2="304.2"/>
      <line x1="603" y1="589.4" x2="789" y2="454"/>
      <line x1="638" y1="697" x2="868" y2="697"/>
    </g>

    <!-- colour band -->
    <path d="M135 912.9 A386 386 0 0 1 69 697 L122 697 A333 333 0 0 0 178.9 883.2 Z" fill="var(--teamwork)"/>
    <path d="M69 697 A386 386 0 0 1 142.7 470.1 L185.6 501.3 A333 333 0 0 0 122 697 Z" fill="var(--empower)"/>
    <path d="M142.7 470.1 A386 386 0 0 1 335.7 329.9 L352.1 380.3 A333 333 0 0 0 185.6 501.3 Z" fill="var(--knowledge)"/>
    <path d="M335.7 329.9 A386 386 0 0 1 574.3 329.9 L557.9 380.3 A333 333 0 0 0 352.1 380.3 Z" fill="var(--proactivity)"/>
    <path d="M574.3 329.9 A386 386 0 0 1 767.3 470.1 L724.4 501.3 A333 333 0 0 0 557.9 380.3 Z" fill="var(--dedication)"/>
    <path d="M767.3 470.1 A386 386 0 0 1 841 697 L788 697 A333 333 0 0 0 724.4 501.3 Z" fill="var(--security)"/>
    <path d="M841 697 A386 386 0 0 1 775 912.9 L731.1 883.2 A333 333 0 0 0 788 697 Z" fill="var(--transparency)"/>

    <!-- band labels -->
    <text class="band-label"><textPath href="#label-arc" startOffset="104.4" text-anchor="middle" dominant-baseline="middle">TEAMWORK</textPath></text>
    <text class="band-label small"><textPath href="#label-arc-outer" startOffset="333.1" text-anchor="middle" dominant-baseline="middle">FINANCIAL</textPath></text>
    <text class="band-label small"><textPath href="#label-arc-inner" startOffset="311.3" text-anchor="middle" dominant-baseline="middle">EMPOWERMENT</textPath></text>
    <text class="band-label"><textPath href="#label-arc" startOffset="540.6" text-anchor="middle" dominant-baseline="middle">KNOWLEDGE</textPath></text>
    <text class="band-label"><textPath href="#label-arc" startOffset="761.8" text-anchor="middle" dominant-baseline="middle">PROACTIVITY</textPath></text>
    <text class="band-label"><textPath href="#label-arc" startOffset="983" text-anchor="middle" dominant-baseline="middle">DEDICATION</textPath></text>
    <text class="band-label"><textPath href="#label-arc" startOffset="1204.1" text-anchor="middle" dominant-baseline="middle">SECURITY</textPath></text>
    <text class="band-label"><textPath href="#label-arc" startOffset="1419.2" text-anchor="middle" dominant-baseline="middle">TRANSPARENCY</textPath></text>

    <!-- grey ring -->
    <path d="M309.5 795.1 A175.5 175.5 0 1 1 600.5 795.1" fill="none" stroke="var(--ring)" stroke-width="15" filter="url(#soft-shadow)"/>

    <!-- pie -->
    <path d="M455 697 L315.7 790.9 A168 168 0 0 1 287 697 Z" fill="var(--teamwork)"/>
    <path d="M455 697 L287 697 A168 168 0 0 1 319.1 598.3 Z" fill="var(--empower)"/>
    <path d="M455 697 L319.1 598.3 A168 168 0 0 1 403.1 537.2 Z" fill="var(--knowledge)"/>
    <path d="M455 697 L403.1 537.2 A168 168 0 0 1 506.9 537.2 Z" fill="var(--proactivity)"/>
    <path d="M455 697 L506.9 537.2 A168 168 0 0 1 590.9 598.3 Z" fill="var(--dedication)"/>
    <path d="M455 697 L590.9 598.3 A168 168 0 0 1 623 697 Z" fill="var(--security)"/>
    <path d="M455 697 L623 697 A168 168 0 0 1 594.3 790.9 Z" fill="var(--transparency)"/>

    <!-- pie icons -->
    <g fill="none" stroke="#fff" stroke-width="2.2" stroke-linecap="round" stroke-linejoin="round">
      <g transform="translate(338.4 732.1)">
        <circle r="16"/><circle cx="0" cy="-16" r="5"/><circle cx="16" cy="0" r="5"/><circle cx="0" cy="16" r="5"/><circle cx="-16" cy="0" r="5"/>
      </g>
      <g transform="translate(340.9 659.9)">
        <circle cx="0" cy="-6" r="10"/><path d="M0 -12 V0 M-3 -9 H3"/>
        <path d="M-20 -2 V10 L-8 18 H8 L20 10 V-2"/>
      </g>
      <g transform="translate(384.5 599.9)">
        <path d="M-7 6 A11 11 0 1 1 7 6 V11 H-7 Z"/><path d="M-5 15 H5"/>
        <path d="M-18 -4 H-22 M18 -4 H22 M-14 -17 L-17 -20 M14 -17 L17 -20"/>
      </g>
      <g transform="translate(455 577)">
        <rect x="-16" y="-20" width="26" height="34" rx="2"/>
        <path d="M-10 -12 H4 M-10 -5 H4 M-10 2 H-2"/>
        <circle cx="10" cy="12" r="9" fill="var(--proactivity)"/><path d="M6 12 L9 15 L14 9"/>
      </g>
      <g transform="translate(525.5 599.9)">
        <path d="M-12 -14 l2 4 4 .5 -3 3 1 4 -4 -2 -4 2 1 -4 -3 -3 4 -.5 Z"/>
        <path d="M0 -16 l2 4 4 .5 -3 3 1 4 -4 -2 -4 2 1 -4 -3 -3 4 -.5 Z"/>
        <path d="M12 -14 l2 4 4 .5 -3 3 1 4 -4 -2 -4 2 1 -4 -3 -3 4 -.5 Z"/>
        <rect x="-20" y="4" width="40" height="12" rx="6"/>
      </g>
      <g transform="translate(569.1 659.9)">
        <path d="M0 -20 L16 -14 V0 C16 10 8 17 0 20 C-8 17 -16 10 -16 0 V-14 Z"/>
        <rect x="-6" y="-2" width="12" height="10" rx="1"/><path d="M-4 -2 V-6 A4 4 0 0 1 4 -6 V-2"/>
      </g>
      <g transform="translate(569.8 732.1)">
        <circle cx="-4" cy="-4" r="13"/><path d="M6 6 L18 18" stroke-width="4"/>
      </g>
    </g>
  </svg>

  <p class="value-copy copy-knowledge">Our team of highly trained and credentialed experts work to educate and lead our clients toward success</p>
  <p class="value-copy copy-proactivity">We hold ourselves accountable in anticipating regulatory changes and keeping you and your plan in compliance</p>
  <p class="value-copy copy-dedication">We provide exceptional customer service and ensure that we are friendly, timely and responsive whenever corresponding with our clients</p>
  <p class="value-copy copy-security">With an emphasis on high technological standards, we lead you toward peace of mind that your savings and investments are protected</p>
  <p class="value-copy copy-transparency">We take pride in representing the retirement plan industry as an open, honest, and socially responsible firm with our clients</p>
  <p class="value-copy copy-teamwork">Collaborating with team members, clients and partners to maintain a high level of communication, accountability and engagement to achieve our common goals</p>
  <p class="value-copy copy-empowerment">We commit ourselves to providing the best retirement solutions to guide our clients toward financial freedom</p>

  <div class="mission-art" role="img" aria-label="Line illustration of two climbers helping each other up toward a summit flag"></div>

  <div class="box-heading our-mission">OUR MISSION</div>
  <p class="mission-text">To proactively support organizations<br>and lead them toward <strong>a secure future</strong></p>

  <footer class="footer"></footer>
  <div class="web-bar">www.summitpensionpartners.com</div>
  <div class="social one"></div>
  <div class="social two"></div>
  <div class="social three"></div>

  <div class="contact">
    <span class="contact-item">
      <svg class="contact-icon" viewBox="0 0 26 26"><circle cx="13" cy="13" r="13" fill="var(--brand-green)"/><path d="M9 7 L11 7 L12 10 L10.5 11.5 C11.5 13.5 12.5 14.5 14.5 15.5 L16 14 L19 15 L19 17 C19 18 18 19 17 19 C12 19 7 14 7 9 C7 8 8 7 9 7 Z" fill="#fff"/></svg>
      555.210.4830
    </span>
    <span class="contact-item">
      <svg class="contact-icon" viewBox="0 0 26 26"><circle cx="13" cy="13" r="13" fill="var(--brand-green)"/><path d="M9 7 L11 7 L12 10 L10.5 11.5 C11.5 13.5 12.5 14.5 14.5 15.5 L16 14 L19 15 L19 17 C19 18 18 19 17 19 C12 19 7 14 7 9 C7 8 8 7 9 7 Z" fill="#fff"/></svg>
      800.555.0192
    </span>
    <span class="contact-item">
      <svg class="contact-icon" viewBox="0 0 26 26"><circle cx="13" cy="13" r="13" fill="var(--brand-green)"/><rect x="7" y="9" width="12" height="9" fill="none" stroke="#fff" stroke-width="1.5"/><path d="M7 9 L13 14 L19 9" fill="none" stroke="#fff" stroke-width="1.5"/></svg>
      info@summitpensionpartners.com
    </span>
  </div>

</div>
</body>
</html>
```